KMRT timeline design

We need a facebook design for our established business which is Australia wide however based in Melbourne. We are a young team of Financial Planners who specialize in Insurance and Basic super advice for people like us.

We are people who help our clients get things done in a timely and cost effective manner whilst having a good time and a laugh along the way.

We do not want it to feel like the standard financial facebook page at all! We would like this to have a consistent feel with our new e-brochure which i have attached from a color and font perspective.

We would also like it to be very easy for people to be able to tell what we do from looking at the page

Reason: Would like time to respond to preferred designs and have re-works done before comitting

Target Market(s)

We work best with client from 25-40 who are time poor singles, young families and self-made entrepreneurs

Industry/Entity Type

Financial

```html
<!DOCTYPE html>
<html lang="en">
<head>
<meta charset="utf-8">
<title>KMRT Planning – Timeline Cover</title>
<link href="https://fonts.googleapis.com/css2?family=Didact+Gothic&family=PT+Sans:wght@400;700&display=swap" rel="stylesheet">
<style>
  :root {
    --page-bg: #eceef1;
    --cover-black: #0b0b0b;
    --photo-light: #8a8a8a;
    --photo-mid: #3a3a3a;
    --brand-green: #1fa84a;
    --band-green: #8dc63f;
    --ink: #111111;
    --profile-dark: #231f20;
    --white: #ffffff;
    --frame-grey: #c9ccd3;
  }
  * { margin: 0; padding: 0; box-sizing: border-box; }
  html, body {
    width: 1200px;
    height: 644px;
    overflow: hidden;
    background: var(--page-bg);
  }
  .stage {
    position: relative;
    width: 1200px;
    height: 644px;
  }
  .timeline-design {
    position: absolute;
    left: 50px;
    top: 86px;
    width: 850px;
    height: 365px;
    transform: scale(1.294);
    transform-origin: top left;
  }
  .cover {
    position: absolute;
    left: 0;
    top: 0;
    width: 850px;
    height: 314px;
    background: var(--cover-black);
    overflow: hidden;
  }
  .cover-photo {
    position: absolute;
    left: 0;
    top: 0;
    width: 580px;
    height: 314px;
    background:
      radial-gradient(ellipse at 22% 30%, var(--photo-light) 0%, var(--photo-mid) 38%, transparent 70%),
      linear-gradient(90deg, var(--photo-mid) 0%, #1c1c1c 55%, var(--cover-black) 100%);
  }
  .cover-brand {
    position: absolute;
    left: 525px;
    top: 30px;
    width: 99px;
    display: flex;
    flex-direction: column;
    align-items: center;
    gap: 10px;
  }
  .cover-brand .brand-square {
    width: 62px;
    height: 62px;
    background: var(--brand-green);
  }
  .cover-brand .brand-name {
    font-family: "Didact Gothic", sans-serif;
    font-size: 28px;
    color: var(--brand-green);
    line-height: 1;
  }
  .tagline {
    position: absolute;
    right: 61px;
    top: 72px;
    font-family: "Didact Gothic", sans-serif;
    font-weight: 400;
    font-size: 45px;
    line-height: 40px;
    color: var(--brand-green);
    text-align: right;
    letter-spacing: 0.5px;
  }
  .tagline .line-first { margin-right: 9px; }
  .contact-band {
    position: absolute;
    left: 402px;
    top: 287px;
    width: 448px;
    height: 27px;
    background: var(--band-green);
    border-radius: 14px 0 0 0;
    font-family: "PT Sans", sans-serif;
    color: var(--ink);
    font-size: 15px;
    line-height: 27px;
    padding-left: 31px;
    white-space: nowrap;
  }
  .contact-band .phone {
    font-weight: 700;
    font-size: 21px;
    vertical-align: -1px;
  }
  .profile-picture {
    position: absolute;
    left: 21px;
    top: 192px;
    width: 172px;
    height: 172px;
    background: var(--profile-dark);
    border: 3px solid var(--white);
    outline: 1px solid var(--frame-grey);
    display: flex;
    flex-direction: column;
    align-items: center;
    justify-content: center;
    gap: 12px;
  }
  .profile-picture .brand-square {
    width: 70px;
    height: 70px;
    background: var(--brand-green);
  }
  .profile-picture .brand-name {
    font-family: "Didact Gothic", sans-serif;
    font-size: 30px;
    color: var(--brand-green);
    line-height: 1;
  }
</style>
</head>
<body>
  <main class="stage">
    <section class="timeline-design">
      <div class="cover">
        <div class="cover-photo" role="img" aria-label="Black and white photo of young business professionals in suits at a meeting"></div>
        <div class="cover-brand">
          <span class="brand-square"></span>
          <span class="brand-name">KMRT</span>
        </div>
        <h1 class="tagline">
          <span class="line-first">SECURE</span><br>
          FUTURE,<br>
          ENHANCED<br>
          LIFESTYLE
        </h1>
        <p class="contact-band">admin@kmrt.com.au | CALL US ON <span class="phone">1300 555 014</span></p>
      </div>
      <div class="profile-picture">
        <span class="brand-square"></span>
        <span class="brand-name">KMRT</span>
      </div>
    </section>
  </main>
</body>
</html>
```